Powerpoint presentation sales pack for ground transfer company

Need a base pack for sales presentation for KLV,
We specialise in corporate ground transport (similar to ZOLTA)
Needs to be sharp and have a modern feel
Looking for a good master slide design and page layout for provide content
Check out our website https://klv.journeys/
Check out our competitors https://www.zolta.com/business https://www.marwickcarservice.com.au
Look at other marketing material available and old draft powerpoint pack for content and design ideas

```html
<!DOCTYPE html>
<html lang="en">
<head>
<meta charset="utf-8">
<title>The KLV Difference</title>
<link rel="stylesheet" href="https://fonts.googleapis.com/css2?family=Carlito:wght@400;700&display=swap">
<style>
  :root {
    --teal: #33b5a0;
    --ink: #4a4a4a;
    --panel: #2b2b2b;
    --paper: #ffffff;
    --light: #f0f0f0;
    --rule: #33b5a0;
  }
  html, body {
    margin: 0;
    padding: 0;
    overflow: hidden;
    background: var(--paper);
  }
  .slide {
    position: relative;
    width: 1200px;
    height: 900px;
    overflow: hidden;
    background: var(--paper);
    font-family: "Carlito", "Calibri", sans-serif;
  }
  .accent-tab {
    position: absolute;
    left: 67px;
    top: 0;
    width: 171px;
    height: 70px;
    background: var(--teal);
  }
  .slide-title {
    position: absolute;
    left: 60px;
    top: 88px;
    margin: 0;
    font-size: 68px;
    font-weight: 700;
    line-height: 1;
    color: var(--ink);
    letter-spacing: -0.5px;
  }
  .slide-title .brand { color: var(--teal); }
  .feature-panel {
    position: absolute;
    left: 0;
    top: 200px;
    width: 1200px;
    height: 650px;
    background: var(--panel);
  }
  .divider {
    position: absolute;
    background: var(--rule);
  }
  .divider.horizontal { left: 0; top: 322px; width: 1158px; height: 1.5px; }
  .divider.v-top { left: 592px; top: 28px; width: 1.5px; height: 294px; }
  .divider.v-left { left: 415px; top: 322px; width: 1.5px; height: 295px; }
  .divider.v-right { left: 798px; top: 322px; width: 1.5px; height: 295px; }
  .feature {
    position: absolute;
    margin: 0;
    font-size: 32px;
    line-height: 1.35;
    color: var(--light);
  }
  .feature strong { font-weight: 400; color: #ffffff; }
  .feature.call-centre { left: 38px; top: 48px; }
  .feature.online-booking { left: 622px; top: 44px; }
  .feature.client-app { left: 38px; top: 348px; }
  .feature.account-management { left: 437px; top: 348px; }
  .feature.account-reporting { left: 815px; top: 348px; }
  .icon {
    position: absolute;
    fill: none;
    stroke: var(--teal);
    stroke-linecap: round;
    stroke-linejoin: round;
  }
  .page-number {
    position: absolute;
    left: 1025px;
    top: 857px;
    font-size: 17px;
    font-weight: 700;
    color: var(--teal);
  }
  .footer-bar {
    position: absolute;
    left: 967px;
    top: 891px;
    width: 175px;
    height: 9px;
    background: var(--teal);
  }
</style>
</head>
<body>
<div class="slide">
  <div class="accent-tab"></div>
  <h1 class="slide-title"><span class="brand">The KLV</span> Difference</h1>

  <section class="feature-panel">
    <div class="divider horizontal"></div>
    <div class="divider v-top"></div>
    <div class="divider v-left"></div>
    <div class="divider v-right"></div>

    <p class="feature call-centre">Australian Based <strong>24 hour Call Centre</strong></p>
    <svg class="icon clock-icon" style="left:212px;top:120px" width="170" height="160" viewBox="0 0 170 160" stroke-width="9">
      <path d="M30 95 A60 60 0 1 0 92 22"/>
      <path d="M18 82 L30 100 L46 84"/>
      <path d="M105 50 L105 85 L80 105"/>
      <g stroke-width="7"><path d="M148 80 L154 80"/><path d="M126 127 L130 133"/><path d="M105 142 L105 148"/><path d="M138 45 L143 41"/></g>
      <text x="10" y="55" fill="#33b5a0" stroke="none" font-family="Carlito, sans-serif" font-weight="700" font-size="34">24hr</text>
    </svg>

    <p class="feature online-booking">Booking 24 hours a day with Easy to<br>Use online booking portal</p>
    <svg class="icon laptop-icon" style="left:795px;top:160px" width="170" height="115" viewBox="0 0 170 115" stroke-width="5">
      <rect x="18" y="6" width="134" height="84" rx="5"/>
      <path d="M4 100 L166 100 L160 110 L10 110 Z"/>
      <path d="M50 56 L58 44 L96 42 L110 52 L122 54 L122 62 L48 62 Z" fill="#33b5a0"/>
      <circle cx="62" cy="63" r="5" fill="#2b2b2b" stroke="none"/>
      <circle cx="108" cy="63" r="5" fill="#2b2b2b" stroke="none"/>
    </svg>

    <p class="feature client-app">Client App for booking<br>and job management</p>
    <svg class="icon phone-icon" style="left:168px;top:458px" width="82" height="160" viewBox="0 0 82 160" stroke-width="3">
      <rect x="4" y="4" width="74" height="152" rx="10"/>
      <path d="M4 22 L78 22 M4 134 L78 134"/>
      <circle cx="41" cy="145" r="5"/>
      <rect x="12" y="30" width="56" height="10" rx="3"/>
      <path d="M12 54 L70 110 M12 110 L40 82 M50 64 L70 84 M12 124 L70 124"/>
      <rect x="28" y="62" width="26" height="10" rx="3"/>
      <circle cx="20" cy="124" r="4"/><circle cx="60" cy="124" r="4"/>
    </svg>

    <p class="feature account-management">Account management<br>with individual traveller<br>preferences</p>
    <svg class="icon user-settings-icon" style="left:545px;top:500px" width="125" height="125" viewBox="0 0 125 125" stroke-width="5">
      <circle cx="48" cy="36" r="22"/>
      <path d="M6 102 A42 38 0 0 1 70 68"/>
      <path d="M6 102 L58 102"/>
      <circle cx="90" cy="94" r="22" stroke-dasharray="9 5" stroke-width="9"/>
      <circle cx="90" cy="94" r="10"/>
    </svg>

    <p class="feature account-reporting">Account Reporting</p>
    <svg class="icon clipboard-icon" style="left:925px;top:462px" width="104" height="146" viewBox="0 0 104 146" stroke-width="4">
      <rect x="4" y="10" width="96" height="132" rx="4"/>
      <rect x="14" y="22" width="76" height="110"/>
      <rect x="34" y="2" width="36" height="16" rx="3"/>
      <g stroke-width="3">
        <path d="M26 48 L30 48 M38 48 L78 48"/>
        <path d="M26 64 L30 64 M38 64 L78 64"/>
        <path d="M26 80 L30 80 M38 80 L78 80"/>
        <path d="M26 96 L30 96 M38 96 L78 96"/>
        <path d="M26 112 L30 112 M38 112 L78 112"/>
      </g>
    </svg>
  </section>

  <div class="page-number">Page 6</div>
  <div class="footer-bar"></div>
</div>
</body>
</html>
```